I need two seperate flyers made
I have supplied 2 x photos of bathrooms, one for each flyer.
First flyer i want a banner or some sort of blockout acccross the bottom with my business name Marlow Bathrooms and my number 0487650923 and the promo is '' Renovate your bathroom from $10990 and in small writing under neath say owner to supply fixtures and tiles

Second flyer to have the same banner accross bottom and the promo is
Complete bathroom renovations from $15990 with small writing under saying terms and conditions apply

Want these to look professional and eye cathcing to generate more work.

I have attached 2x of our old flyers for reference and our current logo for use
Looking forward to working with you.

```html
<!DOCTYPE html>
<html lang="en">
<head>
<meta charset="utf-8">
<title>Marlow Bathrooms – Bathroom Package Flyers</title>
<link href="https://fonts.googleapis.com/css2?family=Anton&family=Montserrat:wght@400;500;600;700;800&display=swap" rel="stylesheet">
<style>
  :root{
    --blue:#0b6fc6;
    --blue-deep:#0a5aa6;
    --ink:#1d1d21;
    --strip:#d8d9db;
    --foot:#d3d3d5;
    --white:#ffffff;
    --page:#ffffff;
    --text-dark:#2a2a2e;
  }
  *{box-sizing:border-box;margin:0;padding:0}
  html,body{width:1200px;height:3557px;overflow:hidden;background:var(--page)}
  body{position:relative;font-family:"Montserrat",Arial,sans-serif}

  .flyer{
    position:absolute;left:120px;width:534px;height:694px;
    background:var(--white);transform:scale(1.8);transform-origin:top left;
    box-shadow:0 2px 10px rgba(0,0,0,.12);overflow:hidden;
  }
  .flyer--renovate{top:353px}
  .flyer--complete{top:1955px}

  .hero-panel{position:absolute;left:0;top:0;width:268px;height:327px;background:var(--blue);color:var(--white)}
  .hero-title{position:absolute;left:30px;top:26px;font-family:"Anton",Impact,sans-serif;font-size:50px;line-height:47px;letter-spacing:.3px;text-transform:uppercase}
  .licence-badge{position:absolute;left:32px;top:140px;width:175px;height:40px}
  .licence-badge__pill{position:absolute;left:12px;top:2px;width:163px;height:36px;background:var(--ink);border-radius:6px}
  .licence-badge__shield{position:absolute;left:0;top:0;width:38px;height:40px}
  .licence-badge__text{position:absolute;left:43px;top:8px;font-size:9.5px;font-weight:800;line-height:10.5px;text-transform:uppercase}
  .tagline{position:absolute;left:32px;top:200px;font-size:11.5px;font-weight:800;text-transform:uppercase}
  .tagline__sub{position:absolute;left:32px;top:216px;font-size:7.6px;font-weight:500}
  .tagline__rule{position:absolute;left:32px;top:235px;width:204px;height:1px;background:rgba(255,255,255,.75)}
  .services{position:absolute;top:251px;list-style:none;font-size:7.6px;font-weight:600;line-height:11px}
  .services--a{left:34px}
  .services--b{left:121px}
  .services li{position:relative;padding-left:13px}
  .services li::before{content:"";position:absolute;left:1px;top:2.5px;width:6px;height:3px;border-left:1.6px solid var(--ink);border-bottom:1.6px solid var(--ink);transform:rotate(-45deg)}

  .photo{position:absolute}
  .photo--hero{left:274px;top:0;width:260px;height:327px}
  .photo--warm{background:linear-gradient(160deg,#ecebe6 0%,#d9d6ce 45%,#b9b4aa 100%)}
  .photo--cool{background:linear-gradient(160deg,#f2f2f2 0%,#d6d7d9 50%,#a9abae 100%)}
  .thumbs{position:absolute;left:31px;top:337px;width:472px;height:103px}
  .thumbs .photo{top:0;width:115px;height:103px;border-radius:18px}
  .thumb-1{left:0}.thumb-2{left:119px}.thumb-3{left:238px}.thumb-4{left:357px}

  .contact-banner{position:absolute;left:31px;top:449px;width:472px;height:207px;background:var(--ink);overflow:hidden}
  .contact-banner__shapes{position:absolute;left:0;top:0;width:472px;height:207px}
  .call-strip{position:absolute;left:8px;top:8px;width:455px;height:48px;background:var(--strip)}
  .call-strip__name{position:absolute;left:39px;top:13px;font-size:10.5px;font-weight:600;line-height:11px;color:var(--blue-deep)}
  .call-strip__cta{position:absolute;left:139px;top:13px;font-size:18.5px;font-weight:500;color:var(--text-dark);white-space:nowrap;display:flex;align-items:center}
  .call-strip__phone{display:inline-flex;align-items:center;margin-left:5px;font-weight:700;color:var(--blue)}
  .call-strip__phone svg{width:10px;height:16px;margin-right:2px}
  .call-strip__rule{position:absolute;left:139px;top:40px;width:278px;height:1px;background:var(--text-dark)}

  .brand{position:absolute;left:44px;top:92px;width:150px;text-align:center;color:var(--blue);font-weight:700;text-transform:uppercase;font-size:14px;line-height:17px;letter-spacing:2.5px}
  .site-link{position:absolute;left:44px;top:166px;width:148px;height:13px;border:1px solid #cfcfd2;color:#e8e8ea;font-size:5.8px;font-weight:500;text-align:center;line-height:11px}

  .promo{position:absolute;left:261px;top:92px;color:var(--white)}
  .promo__lead{font-size:11.4px;font-weight:700;line-height:12px;text-transform:uppercase}
  .promo__price{font-size:30px;font-weight:800;line-height:33px;letter-spacing:-.3px}
  .promo__note{font-size:6.3px;font-weight:500}

  .flyer__foot{position:absolute;left:0;top:645px;width:534px;height:49px;background:var(--foot);z-index:-0}
  .contact-banner{z-index:1}
</style>
</head>
<body>

<!-- Flyer one: renovation package -->
<article class="flyer flyer--renovate">
  <div class="flyer__foot"></div>
  <section class="hero-panel">
    <h1 class="hero-title">Bathroom<br>Package</h1>
    <div class="licence-badge">
      <div class="licence-badge__pill"></div>
      <svg class="licence-badge__shield" viewBox="0 0 38 40"><path d="M19 2 L34 7 V19 C34 29 27 35 19 38 C11 35 4 29 4 19 V7 Z" fill="#fff"/><path d="M19 6 L30 10 V19 C30 27 25 31.5 19 34 C13 31.5 8 27 8 19 V10 Z" fill="#1d1d21"/><path d="M13 20 L17.5 24.5 L26 15" fill="none" stroke="#fff" stroke-width="2.6" stroke-linecap="round" stroke-linejoin="round"/></svg>
      <p class="licence-badge__text">Fully licensed &amp;<br>insured</p>
    </div>
    <h2 class="tagline">Built to last</h2>
    <p class="tagline__sub">Your local renovation specialists</p>
    <div class="tagline__rule"></div>
    <ul class="services services--a"><li>Demolition</li><li>Electrical</li><li>Carpentry</li><li>Tiling</li></ul>
    <ul class="services services--b"><li>Waterproofing</li><li>Plumbing</li><li>Design<br>Consultation</li></ul>
  </section>
  <div class="photo photo--hero photo--warm" role="img" aria-label="Photo of a finished bathroom with oval mirror, floating vanity, brass shower and glass screen"></div>
  <div class="thumbs">
    <div class="photo thumb-1 photo--cool" role="img" aria-label="Photo of a tiled bathroom with window and vanity"></div>
    <div class="photo thumb-2 photo--warm" role="img" aria-label="Photo of a round basin with brass mixer tap"></div>
    <div class="photo thumb-3 photo--cool" role="img" aria-label="Photo of a framed glass shower enclosure"></div>
    <div class="photo thumb-4 photo--warm" role="img" aria-label="Photo of a freestanding bath beside a window"></div>
  </div>
  <section class="contact-banner">
    <svg class="contact-banner__shapes" viewBox="0 0 472 207">
      <polygon points="222,0 472,0 472,207 292,207 211,126 262,74" fill="#0b6fc6"/>
      <polyline points="266,72 211,126 282,197" fill="none" stroke="#fff" stroke-width="3"/>
      <polygon points="196,70 224,80 214,88" fill="#fff"/>
      <polygon points="226,80 232,92 222,90" fill="#0b6fc6"/>
      <polygon points="412,150 422,158 416,160" fill="#fff"/>
      <polygon points="420,162 444,176 438,190" fill="#1d1d21"/>
    </svg>
    <div class="call-strip">
      <p class="call-strip__name">Marlow<br>Bathrooms</p>
      <p class="call-strip__cta">Call Us Now <span class="call-strip__phone"><svg viewBox="0 0 10 16"><path d="M8 1 C4 2 2 5 2 8 C2 11 4 14 8 15 L9 12 L6.5 11 C5.5 10 5.5 6 6.5 5 L9 4 Z" fill="#0b6fc6"/></svg>0487650923</span></p>
      <div class="call-strip__rule"></div>
    </div>
    <p class="brand">Marlow<br>Bathrooms</p>
    <p class="site-link">www.marlowbathrooms.com.au</p>
    <div class="promo">
      <p class="promo__lead">Renovate your<br>bathroom from</p>
      <p class="promo__price">$10990</p>
      <p class="promo__note">Owner to supply Fixtures &amp; Tiles</p>
    </div>
  </section>
</article>

<!-- Flyer two: complete renovations -->
<article class="flyer flyer--complete">
  <div class="flyer__foot"></div>
  <section class="hero-panel">
    <h1 class="hero-title">Bathroom<br>Package</h1>
    <div class="licence-badge">
      <div class="licence-badge__pill"></div>
      <svg class="licence-badge__shield" viewBox="0 0 38 40"><path d="M19 2 L34 7 V19 C34 29 27 35 19 38 C11 35 4 29 4 19 V7 Z" fill="#fff"/><path d="M19 6 L30 10 V19 C30 27 25 31.5 19 34 C13 31.5 8 27 8 19 V10 Z" fill="#1d1d21"/><path d="M13 20 L17.5 24.5 L26 15" fill="none" stroke="#fff" stroke-width="2.6" stroke-linecap="round" stroke-linejoin="round"/></svg>
      <p class="licence-badge__text">Fully licensed &amp;<br>insured</p>
    </div>
    <h2 class="tagline">Built to last</h2>
    <p class="tagline__sub">Your local renovation specialists</p>
    <div class="tagline__rule"></div>
    <ul class="services services--a"><li>Demolition</li><li>Electrical</li><li>Carpentry</li><li>Tiling</li></ul>
    <ul class="services services--b"><li>Waterproofing</li><li>Plumbing</li><li>Design<br>Consultation</li></ul>
  </section>
  <div class="photo photo--hero photo--cool" role="img" aria-label="Photo of a white bathroom with backlit round mirror, shaker vanity and built-in bath"></div>
  <div class="thumbs">
    <div class="photo thumb-1 photo--warm" role="img" aria-label="Photo of a brass wall tap over a round basin"></div>
    <div class="photo thumb-2 photo--cool" role="img" aria-label="Photo of a white basin with black mixer tap"></div>
    <div class="photo thumb-3 photo--cool" role="img" aria-label="Photo of a bathroom with bath and shower niche"></div>
    <div class="photo thumb-4 photo--cool" role="img" aria-label="Photo of a backlit oval mirror on white tiles"></div>
  </div>
  <section class="contact-banner">
    <svg class="contact-banner__shapes" viewBox="0 0 472 207">
      <polygon points="222,0 472,0 472,207 292,207 211,126 262,74" fill="#0b6fc6"/>
      <polyline points="266,72 211,126 282,197" fill="none" stroke="#fff" stroke-width="3"/>
      <polygon points="196,70 224,80 214,88" fill="#fff"/>
      <polygon points="226,80 232,92 222,90" fill="#0b6fc6"/>
      <polygon points="412,150 422,158 416,160" fill="#fff"/>
      <polygon points="420,162 444,176 438,190" fill="#1d1d21"/>
    </svg>
    <div class="call-strip">
      <p class="call-strip__name">Marlow<br>Bathrooms</p>
      <p class="call-strip__cta">Call Us Now <span class="call-strip__phone"><svg viewBox="0 0 10 16"><path d="M8 1 C4 2 2 5 2 8 C2 11 4 14 8 15 L9 12 L6.5 11 C5.5 10 5.5 6 6.5 5 L9 4 Z" fill="#0b6fc6"/></svg>0487650923</span></p>
      <div class="call-strip__rule"></div>
    </div>
    <p class="brand">Marlow<br>Bathrooms</p>
    <p class="site-link">www.marlowbathrooms.com.au</p>
    <div class="promo">
      <p class="promo__lead">Complete bathroom<br>renovations from</p>
      <p class="promo__price">$15990</p>
      <p class="promo__note">Terms and Conditions apply</p>
    </div>
  </section>
</article>

</body>
</html>
```